Wordpress design for my private practice website - Psychotherapist

I would like a simple, clean, and elegant design for my private practice website. I work with both adults and children so I'd like it to appeal to both. However, since parents make the choice as to where to send their child for therapy, I want it to appeal to adults more. I would like the pictures on the site to have a calming effect - maybe using sand and water and rocks. I am attaching files with my company logo. I would also like my name incorporated into the header - Rosalind Vantreece, LCSW, Registered Play Therapist. I've also uploaded a picture of myself for my About Page.

I like the design of these 2 website and want something similar:
www.drmaribelostrand.com
www.harrowgate-lisk.com

I would like a home page that highlights a calming graphic across the entire top of the page as well as my practice logo and my name.

I'd like a link to social media sites on the top of the homepage - facebook, pinterest.

I want a simple bar across the top with the following tabs:
Home
About Me (subtabs Who I Am, Specialties and Approach)
Counseling Services (subtabs Individual Counseling, Play Therapy, Sandplay Therapy,)
Fees
FAQs
Contact Me (would love this to be a fill in the blank contact form that sends info to my email address - should include name, phone number, email and a comment box for more information requested)
Blog (this will link with another wordpress blog)

Target Market(s)

Parents of children under age 12 with behavioral problems or are dealing with the breakup of their family through divorce - looking for someone to work with their young child. I also work with Adults that are overwhelmed and worried - often women that have many life stressors and are feeling burnt out on life and meeting everyone's needs. Families going through some type of trauma, including divorce or grief work. I also work with individuals going through a transition of religious beliefs - often exiting the religion of their youth and undergoing a crisis of faith at midlife.

Industry/Entity Type

Mental Health

Contact Information for Business Card

Rosalind Vantreece, LCSW
Registered Play Therapist
4815 Bellhaven Court
Idaho Falls, Idaho 83404
(208)555-7162
www.stillbrookwellness.com

On the opposite side, I'd like an appointment reminder area - with the following text:

Your next appointment is
_____/______/______ at ______am/pm
Please give 24 hrs notice if you need to cancel your appointment.

Coding

Coded - Design and coding required

Number of Pages Required

5+ page

Font styles to use
Sans Serif

Colors
33a6d7
9bcb3c
0355a3

Requirements
Must have
• I'd like it to be a wordpress site. I'm such a newby at web design - but I need to be able to add content and manage the site myself once it is up and running.
Nice to have
• I like the design of these 2 websites and want something similar:
• www.drmaribelostrand.com
• www.harrowgate-lisk.com
• They are clean, easy to navigate and calming.
Should not have
• Should not look like a childcare website.

```html
<!DOCTYPE html>
<html lang="en">
<head>
<meta charset="utf-8">
<title>Stillbrook Wellness — About</title>
<link href="https://fonts.googleapis.com/css2?family=Open+Sans:wght@300;400;600&family=EB+Garamond:wght@600&family=Petit+Formal+Script&display=swap" rel="stylesheet">
<style>
  :root {
    --brand-deep: #0355a3;
    --ink: #4a4a4a;
    --ink-soft: #6b6b6b;
    --text-muted: #7a7a7a;
    --page-bg: #edebec;
    --header-bg: #ffffff;
    --footer-bg: #f4f3f3;
    --dropdown-bg: #9a9a9a;
    --dropdown-line: #b4b4b4;
    --icon-grey: #dcdcdc;
    --icon-dark: #5a5a5a;
    --hero-top: #aa9eb0;
    --hero-mid: #cbb6bc;
    --hero-low: #c9aab6;
    --hero-bottom: #a991a8;
  }
  * { margin: 0; padding: 0; box-sizing: border-box; }
  html, body { width: 1200px; height: 1148px; overflow: hidden; }
  body {
    position: relative;
    background: var(--page-bg);
    font-family: "Open Sans", Arial, sans-serif;
    color: var(--text-muted);
  }

  .site-header {
    position: absolute; left: 0; top: 0; width: 1200px; height: 144px;
    background: var(--header-bg);
  }
  .brand {
    position: absolute; left: 0; top: 20px; width: 1200px;
    text-align: center; color: var(--brand-deep);
  }
  .brand-mark {
    display: block; width: 44px; height: 44px; margin: 0 auto 10px;
    border-radius: 50%; background: var(--brand-deep);
  }
  .brand-name {
    display: block; font-weight: 300; font-size: 18px; letter-spacing: 5px;
    text-transform: uppercase; line-height: 22px;
  }
  .brand-tag {
    display: block; font-weight: 300; font-size: 9px; letter-spacing: 4px;
    text-transform: uppercase; margin-top: 2px;
  }
  .header-social {
    position: absolute; left: 1024px; top: 104px; display: flex; gap: 12px;
  }
  .header-social span {
    width: 11px; height: 11px; border-radius: 50%; background: var(--icon-dark);
  }

  .hero {
    position: absolute; left: 0; top: 144px; width: 1200px; height: 335px;
    background: linear-gradient(180deg, var(--hero-top) 0%, var(--hero-mid) 45%, var(--hero-low) 72%, var(--hero-bottom) 100%);
  }
  .hero-title {
    position: absolute; left: 83px; top: 140px; color: var(--ink);
  }
  .hero-title h1 {
    font-family: "EB Garamond", Georgia, serif; font-weight: 600;
    font-size: 29px; line-height: 32px;
  }
  .hero-title p {
    font-family: "Petit Formal Script", cursive; font-size: 15px;
    line-height: 22px; color: var(--ink);
  }

  .main-nav {
    position: absolute; left: 0; top: 479px; width: 1200px; height: 75px;
    background: linear-gradient(180deg, #fafafa, #f1f1f1);
    box-shadow: 0 2px 3px rgba(0,0,0,.08);
  }
  .main-nav a {
    position: absolute; top: 28px; font-size: 15px; color: var(--ink);
    text-decoration: none; line-height: 20px;
  }
  .main-nav .has-sub::after {
    content: ""; display: inline-block; width: 5px; height: 5px;
    border-right: 1px solid #999; border-bottom: 1px solid #999;
    transform: rotate(45deg); margin-left: 5px; position: relative; top: -3px;
  }

  .dropdown {
    position: absolute; left: 455px; top: 554px; width: 153px;
    background: var(--dropdown-bg); list-style: none;
  }
  .dropdown li {
    height: 31px; line-height: 31px;
    text-align: center; color: #fff; font-size: 11px; text-transform: uppercase;
    border-bottom: 1px solid var(--dropdown-line);
  }
  .dropdown li:first-child { height: 37px; line-height: 44px; }
  .dropdown li:last-child { border-bottom: none; }

  .portrait {
    position: absolute; left: 84px; top: 679px; width: 298px; height: 298px;
    border-radius: 50%;
    background: radial-gradient(circle at 50% 45%, #e6c99a 0%, #d3b47a 55%, #9c8a5a 100%);
    box-shadow: 2px 4px 8px rgba(0,0,0,.25);
  }

  .about {
    position: absolute; left: 445px; top: 612px; width: 662px;
  }
  .about h2 {
    text-align: center; font-weight: 600; font-size: 26px; color: var(--ink-soft);
    line-height: 40px; margin-bottom: 22px;
  }
  .about p {
    font-size: 12px; line-height: 21px; color: var(--text-muted);
    letter-spacing: -0.1px; margin-bottom: 42px;
    hyphens: auto;
  }

  .site-footer {
    position: absolute; left: 0; top: 1045px; width: 1200px; height: 103px;
    background: var(--footer-bg); border-top: 2px solid #e2e0e1; text-align: center;
  }
  .site-footer p { font-size: 12.5px; color: var(--text-muted); margin-top: 22px; }
  .footer-social {
    display: flex; justify-content: center; gap: 9px; margin-top: 14px;
  }
  .footer-social span {
    width: 22px; height: 22px; border-radius: 50%; background: var(--icon-grey);
  }
</style>
</head>
<body>
  <header class="site-header">
    <div class="brand">
      <span class="brand-mark"></span>
      <span class="brand-name">Stillbrook</span>
      <span class="brand-tag">Wellness</span>
    </div>
    <div class="header-social" aria-label="Social links">
      <span></span><span></span><span></span>
    </div>
  </header>

  <section class="hero" role="img" aria-label="Calming photo of stacked stones against a soft pink and lavender sunset sky">
    <div class="hero-title">
      <h1>Rosalind Vantreece,</h1>
      <p>Relationship Counselor</p>
    </div>
  </section>

  <nav class="main-nav">
    <a class="has-sub" style="left:303px">Home</a>
    <a style="left:383px">About</a>
    <a class="has-sub" style="left:463px">Counseling Services</a>
    <a style="left:632px">Fees</a>
    <a style="left:702px">FAQs</a>
    <a style="left:776px">Contact</a>
    <a style="left:867px">Blog</a>
  </nav>

  <div class="portrait" role="img" aria-label="Portrait photo of the counselor"></div>

  <main class="about" lang="en">
    <h2>ABOUT</h2>
    <p>Lorem ipsum dolor sit amet, consectetur adipiscing elit. Quisque nec tempor nunc. Proin vestibulum lacinia metus, vitae efficitur est luctus sed. Etiam neque felis, ullamcorper eu urna quis, consectetur pulvinar tortor. Vestibulum ullamcorper semper nisi, pretium molestie tortor scelerisque eu. Phasellus quis leo id leo tempus rutrum in eu massa. Ut felis nulla, dapibus id malesuada et, sodales eget velit. Aenean facilisis arcu quis pellentesque rhoncus. Nunc tempus ex vitae arcu sodales, eu efficitur est luctus. Nullam dolor leo, ornare vel faucibus vel, porta vel est. Phasellus at mauris id nunc mattis commodo vitae eget elit. Quisque et gravida nisi. Pellentesque sagittis mauris et iaculis volutpat. Ut vehicula a libero ultricies mattis. Ut cursus ligula auctor, vestibulum dolor eget, lobortis nibh. Fusce molestie volutpat interdum.</p>
    <p>Nunc tempus ex vitae arcu sodales, eu efficitur est luctus. Nullam dolor leo, ornare vel faucibus vel, porta vel est. Phasellus at mauris id nunc mattis commodo vitae eget elit. Quisque et gravida nisi. Pellentesque sagittis mauris et iaculis volutpat.</p>
  </main>

  <ul class="dropdown">
    <li>Individual Counseling</li>
    <li>Play Therapy</li>
    <li>Sandplay Therapy</li>
  </ul>

  <footer class="site-footer">
    <p>© 2012 Rosalind Vantreece. All rights reserved.</p>
    <div class="footer-social" aria-label="Social links">
      <span></span><span></span><span></span><span></span>
    </div>
  </footer>
</body>
</html>
```